Healthcare recruitment agency - Brochure Design Project

We are looking to develop a new brochure for our business. Rather than a brochure we will actually have 4 x A4 double sided flyers.
Each flyer will have the same content on front side and sector specific content on the back page.
The sectors will be:
a. Homelessness & Substance Misuse
b. Elderly Care
c. Learning Disabilities
d. Mental Health
It is important for us to get the base design right as this will follow suit across all our communications, the winning designer will get more work including mouse mat, folder and further flyers.
We are a people orientated business for both our staff and the people who they care for, imagery is important and we will source the final images (a couple attached to start things rolling).
I also like the idea of a people montage (see eye montage for an idea of what i mean) This could help describe the varied healthcare element of what we do and extend to other marketing materials with the relevant image highlighted from the rest.
Initially focus on 1 x double sided A4 flyer so we can get the design right, then we can go from there! Also attached is some copy to add to the initial flyer to help the concept develop.
Once the base design has been agreed, images and copy will be sent for the other x3 flyers to make up the equivalent of an 8pp brochure, although x4 pages will be identical.
The first page is generic about the company
The second page is on 'homeless and substance misuse' support staff.
Update: I have just added a file (velo logo) this is the group logo that should be on the front page somewhere. Plus a AI version of the Tarsk logo.
Updates
Hi Guys,
Target Market(s)
Healthcare and social care market, care managers, senior healthcare buyers
Industry/Entity Type
Healthcare
Requirements
Must have
- Our logo and group logo
Use our colours of green, grey and plum (in that order)

```html
<!DOCTYPE html>
<html lang="en">
<head>
<meta charset="utf-8">
<title>Tarsk – Homelessness &amp; Substance Misuse</title>
<link href="https://fonts.googleapis.com/css2?family=Source+Sans+3:wght@400&family=PT+Sans+Narrow:wght@400&display=swap" rel="stylesheet">
<style>
  :root {
    --sage-bg: #d3dab8;
    --sage-edge: #c2cc9e;
    --green: #8da957;
    --grey: #6d6e70;
    --grey-text: #5d5e60;
    --plum: #9b2b7e;
    --white: #ffffff;
  }
  * { margin: 0; padding: 0; box-sizing: border-box; }
  html, body { width: 852px; height: 1200px; overflow: hidden; }
  body {
    position: relative;
    background: linear-gradient(180deg, var(--sage-bg) 0%, #dde3c6 100%);
    font-family: "Source Sans 3", Arial, sans-serif;
    color: var(--grey-text);
  }
  .edge-strip {
    position: absolute; left: 32px; top: 86px; width: 18px; height: 1034px;
    background: var(--sage-edge);
  }
  .card-top {
    position: absolute; left: 50px; top: 58px; width: 539px; height: 510px;
    background: var(--white);
  }
  .card-bottom {
    position: absolute; left: 50px; top: 678px; width: 539px; height: 457px;
    background: var(--white);
  }
  .montage {
    position: absolute; left: 589px; width: 263px;
    background: linear-gradient(160deg, #8a6a5a 0%, #b9957f 25%, #6f5a52 50%, #a88b78 75%, #5e4d46 100%);
  }
  .montage-top { top: 0; height: 568px; }
  .montage-bottom { top: 678px; height: 522px;
    background: linear-gradient(200deg, #6b5750 0%, #a08474 30%, #3f3634 55%, #b5967f 80%, #7a6458 100%); }

  .brand-name {
    position: absolute; left: 94px; top: 128px;
    font-family: "Source Sans 3", Arial, sans-serif; font-weight: 400;
    font-size: 112px; line-height: 1; color: var(--grey); letter-spacing: -1px;
  }

  .sector-title {
    position: absolute; left: 92px; top: 330px;
    font-family: "PT Sans Narrow", Arial, sans-serif; font-weight: 400;
    font-size: 39px; line-height: 44px; color: var(--grey); letter-spacing: -0.3px;
  }
  .sector-title .amp { font-size: 29px; }
  .highlights {
    position: absolute; left: 110px; top: 389px; width: 340px;
    list-style: none; font-size: 16.5px; line-height: 21px; color: var(--grey-text);
  }
  .highlights li { position: relative; padding-left: 18px; margin-bottom: 9px; }
  .highlights li::before {
    content: ""; position: absolute; left: 2px; top: 9px;
    width: 4px; height: 4px; border-radius: 50%; background: var(--grey);
  }

  .intro-band {
    position: absolute; left: 50px; top: 568px; width: 539px; height: 96px;
    background: var(--green); color: var(--white);
    padding: 10px 18px 0 42px;
    font-size: 20.5px; line-height: 29px;
  }
  .plum-rule {
    position: absolute; left: 0; top: 664px; width: 852px; height: 14px;
    background: var(--plum);
  }

  .body-copy {
    position: absolute; left: 91px; top: 714px; width: 472px;
    font-size: 16.5px; line-height: 23px; color: var(--grey-text);
  }
  .body-copy p { margin-bottom: 23px; }
</style>
</head>
<body>
  <div class="edge-strip"></div>
  <div class="card-top"></div>
  <div class="card-bottom"></div>

  <div class="montage montage-top" role="img" aria-label="Montage of close-up photographs of many different people's eyes"></div>
  <div class="montage montage-bottom" role="img" aria-label="Montage of close-up photographs of many different people's eyes"></div>

  <div class="brand-name">Tarsk</div>

  <h1 class="sector-title">Homelessness <span class="amp">&amp;</span> Substance Misuse</h1>
  <ul class="highlights">
    <li>We currently provide staff to homeless and substance misuse organisations</li>
    <li>Tarsk have experienced and fully compliant staff ready to work now across London</li>
    <li>Bespoke training provided on request</li>
    <li>Swedish Derogation staff available</li>
  </ul>

  <div class="intro-band">We are a leading supplier of support / project workers and key workers to a number of London's homeless and substance misuse organisations.</div>
  <div class="plum-rule"></div>

  <div class="body-copy">
    <p>We are fully aware that the role within this specific area is varied, requiring an interactive person who is happy to get involved.</p>
    <p>'Support Worker' has such a varied meaning and not all support workers are suitable to this type of work, we work hard to ensure that relevant staff are trained in-house to assess their suitability.</p>
    <p>As a new client the first element that you would expect is that one of our Account Managers will visit each of your services or projects to gain a full understanding the levels of support that are required and prepare this information so staff are completely briefed before they attend.</p>
    <p>Our staff will have experience of working alongside the homeless and drug and alcohol misuse or have relevant transferable skills and experience to ensure you get great supplements to your team.</p>
  </div>
</body>
</html>
```